Corvantis websites redesign

Www.cor-vantis.com needs to be redesigned along with updations. The incremental material will be provided for the updations. We are looking for complete redesign of the pages with the new content. The complete write up will be provided soon

Target Market(s)

Global

Coding

Coded - Design and coding required

Number of Pages Required

5+ page

Requirements
Must have
• A clean and slick design for the Consulting.
Should not have
• Too many pictures which reduces the speed of the site

```html
<!DOCTYPE html>
<html lang="en">
<head>
<meta charset="utf-8">
<title>Corvantis Consultancy</title>
<link rel="stylesheet" href="https://fonts.googleapis.com/css2?family=Roboto+Condensed:wght@400;700&family=Open+Sans:wght@400;600;700&family=Raleway:wght@300;400&display=swap">
<style>
:root{
  --blue:#1b8ad0;
  --navy:#1f2a44;
  --maroon:#4a1a22;
  --text:#555b63;
  --light:#efefef;
  --case:#2f3d59;
  --white:#ffffff;
  --grey-icon:#9aa0a6;
}
*{box-sizing:border-box;margin:0;padding:0}
html,body{width:1200px;height:2675px;overflow:hidden;background:var(--white)}
body{position:relative;font-family:"Open Sans",sans-serif;color:var(--text)}
.abs{position:absolute}

.hero{left:0;top:0;width:1200px;height:668px;background:linear-gradient(160deg,#e6ecef 0%,#cfd6dc 45%,#b9c2ca 100%)}
.brand{left:0;top:262px;width:1200px;display:flex;justify-content:center;align-items:center;gap:22px}
.brand-dot{width:90px;height:90px;border-radius:50%;background:var(--blue)}
.brand-name{font-family:"Open Sans",sans-serif;font-weight:600;font-size:82px;color:var(--maroon);letter-spacing:-1px}

.nav{left:0;top:668px;width:1200px;height:60px;background:rgba(200,205,210,.75);border-top:2px solid var(--navy);display:flex;align-items:center}
.nav a{position:absolute;font-family:"Roboto Condensed",sans-serif;font-size:20px;color:#111;text-decoration:none;height:58px;line-height:58px}
.nav a.active{background:var(--blue);color:var(--white);padding:0 25px}
.nav-rule{left:0;top:728px;width:1200px;height:7px;background:var(--navy)}
.notch{width:0;height:0;border-left:12px solid transparent;border-right:12px solid transparent;border-top:12px solid var(--navy)}
.shade{height:40px;background:radial-gradient(ellipse at top,rgba(0,0,0,.28) 0%,rgba(0,0,0,0) 70%)}

.welcome-title{left:80px;top:818px;font-family:"Roboto Condensed",sans-serif;font-size:41px;color:var(--maroon)}
.welcome-title span{color:var(--blue)}
.welcome-text{left:80px;top:890px;width:625px;font-size:16px;line-height:26px}
.btn-more{left:78px;top:1022px;width:156px;height:45px;background:var(--navy);color:var(--white);font-family:"Roboto Condensed",sans-serif;font-size:20px;border-radius:3px;display:flex;align-items:center;justify-content:center}
.mark{left:790px;top:815px;width:258px;height:258px;border-radius:50%;background:var(--navy)}

.callbox{left:77px;top:1127px;width:1046px;height:210px;background:var(--light);border-bottom:5px solid var(--navy)}
.call-note{left:0;top:35px;width:1046px;text-align:center;font-size:15px;line-height:25px}
.call-row{left:0;top:108px;width:1046px;display:flex;justify-content:center;align-items:center;gap:18px;font-family:"Roboto Condensed",sans-serif;font-size:31px;color:var(--navy)}
.call-row b{font-weight:700}

.section-title{left:0;width:1200px;text-align:center;font-family:"Roboto Condensed",sans-serif;font-size:41px;color:var(--blue)}
.section-sub{left:0;top:1475px;width:1200px;text-align:center;font-size:15px;line-height:26px}
.service{width:520px;text-align:center}
.service-icon{margin:0 auto;width:124px;height:124px;border-radius:50%;background:var(--navy);display:flex;align-items:center;justify-content:center}
.service h3{margin-top:34px;font-family:"Roboto Condensed",sans-serif;font-weight:400;font-size:25px;color:var(--blue)}
.service p{margin-top:8px;font-size:15px;line-height:25px}
.divider{left:599px;top:1551px;width:1px;height:335px;background:#d6d6d6}

.case{left:0;top:1915px;width:1200px;height:467px;background:linear-gradient(180deg,#2c3a56 0%,#3a4760 60%,#4a5468 100%)}
.case-title{left:0;top:50px;width:1200px;text-align:center;font-family:"Raleway",sans-serif;font-weight:300;font-size:47px;color:var(--white)}
.case-sub{left:0;top:122px;width:1200px;text-align:center;font-size:15px;line-height:26px;color:var(--white)}
.case-facts{left:0;top:190px;width:1200px;text-align:center;font-size:21px;line-height:31px;color:var(--white)}
.case-facts b{font-weight:700}
.arrow{width:64px;height:64px;border:2px solid var(--white);border-radius:50%;display:flex;align-items:center;justify-content:center}
.case-btn{left:225px;top:337px;width:750px;height:57px;background:var(--blue);color:var(--white);font-weight:700;font-size:20px;display:flex;align-items:center;justify-content:center;border-radius:2px}

.to-top{left:564px;top:2408px;width:72px;height:72px;border:4px solid var(--blue);border-radius:50%;display:flex;align-items:center;justify-content:center}
.copyright{left:0;top:2496px;width:1200px;text-align:center;font-size:14px;color:#333}
.copyright span{color:var(--blue);font-weight:700}
.social{width:50px;height:50px;border-radius:50%;background:var(--grey-icon);border:3px solid #e3e3e3;top:2542px}
.social.dark{background:var(--navy)}
.footer-bar{left:0;top:2648px;width:1200px;height:27px;background:var(--navy);border-top:4px solid var(--blue)}
</style>
</head>
<body>

<div class="abs hero" role="img" aria-label="Photo of business people shaking hands at a meeting table"></div>
<div class="abs brand"><div class="brand-dot"></div><div class="brand-name">Corvantis</div></div>

<nav class="abs nav">
  <a class="active" style="left:87px">HOME</a>
  <a style="left:230px">FOUNDER</a>
  <a style="left:379px">CONSULTANCY</a>
  <a style="left:578px">SYSTEM</a>
  <a style="left:716px">CASE STUDIES</a>
  <a style="left:905px">CONTACT</a>
</nav>
<div class="abs nav-rule"></div>
<div class="abs notch" style="left:588px;top:735px"></div>
<div class="abs shade" style="left:20px;top:735px;width:1160px"></div>

<h1 class="abs welcome-title">WELCOME TO <span>CORVANTIS</span></h1>
<p class="abs welcome-text">Corvantis Consultancy Limited capitalizes on synergies arising from trade and investment linkages between countries and knowledge of traditional and non-traditional pools of liquidity to provide consultancy services to Emerging country banks, Corporates and SMEs.</p>
<div class="abs btn-more">READ MORE</div>
<div class="abs mark"></div>

<section class="abs callbox">
  <p class="abs call-note">Lorem Ipsum is simply dummy text of the printing and typesetting industry. Lorem<br>Ipsum has been the industry.</p>
  <div class="abs call-row">
    <span>CALL US ON</span>
    <svg width="64" height="64" viewBox="0 0 64 64"><circle cx="32" cy="32" r="30" fill="none" stroke="#1f2a44" stroke-width="2"/><path d="M22 20c2-2 4-2 5 0l3 5c1 2 0 3-1 4l-2 2c1 3 4 6 7 8l2-2c1-1 2-2 4-1l5 3c2 1 2 3 0 5l-2 2c-3 3-10 0-16-6s-9-13-6-16z" fill="#1f2a44"/></svg>
    <b>+852-21004417</b>
  </div>
</section>
<div class="abs notch" style="left:588px;top:1337px"></div>
<div class="abs shade" style="left:90px;top:1342px;width:1020px"></div>

<h2 class="abs section-title" style="top:1412px">CONSULTANCY</h2>
<p class="abs section-sub">CVL will work with you to understand your business and offer need based strategic and transactional advice<br>which fits your corporate strategy.</p>

<div class="abs service" style="left:70px;top:1557px">
  <div class="service-icon">
    <svg width="80" height="80" viewBox="0 0 80 80"><circle cx="40" cy="40" r="24" fill="none" stroke="#fff" stroke-width="5"/><circle cx="40" cy="16" r="9" fill="#fff"/><circle cx="19" cy="52" r="9" fill="#fff"/><circle cx="61" cy="52" r="9" fill="#fff"/></svg>
  </div>
  <h3>PLAIN VANILLA FINANCING SOLUTIONS</h3>
  <p>The Consultancy provides access to local/regional banks across Hong Kong, Singapore, Dubai , New York and London and helps corporate clients in diversifying their financial partners and adding new banks to their bank group.</p>
</div>
<div class="abs divider"></div>
<div class="abs service" style="left:608px;top:1557px">
  <div class="service-icon">
    <svg width="80" height="80" viewBox="0 0 80 80" fill="#fff"><rect x="30" y="10" width="20" height="16" rx="2"/><rect x="38" y="26" width="4" height="12"/><rect x="16" y="36" width="48" height="4"/><rect x="16" y="36" width="4" height="12"/><rect x="38" y="36" width="4" height="12"/><rect x="60" y="36" width="4" height="12"/><rect x="8" y="48" width="20" height="18" rx="2"/><rect x="30" y="48" width="20" height="18" rx="2"/><rect x="52" y="48" width="20" height="18" rx="2"/></svg>
  </div>
  <h3>STRUCTURED FINANCING SOLUTIONS</h3>
  <p>The Consultancy provides end-to-end structured solutions on the Payables, Receivables or Inventory side for working capital requirements with off/part/on recourse balance sheet structures. We also specialize in providing credit enhancements...</p>
</div>

<section class="abs case" role="img" aria-label="Dusky photo of a cable-stayed bridge under a dark blue sky">
  <h2 class="abs case-title">CASE STUDY</h2>
  <p class="abs case-sub">Some of the deals completed by CVL are summarised below to describe the range of activities undertaken<br>with Corporates.</p>
  <div class="abs case-facts">
    <b>Annual turnover of customer :</b> New Company<br>
    <b>Annual group turnover:</b> Over USD 550.0 million<br>
    <b>Facility Arranged :</b> USD 8.4 million
  </div>
  <div class="abs arrow" style="left:45px;top:171px"><svg width="20" height="34" viewBox="0 0 20 34"><path d="M16 2L4 17l12 15" fill="none" stroke="#fff" stroke-width="2"/></svg></div>
  <div class="abs arrow" style="left:1089px;top:171px"><svg width="20" height="34" viewBox="0 0 20 34"><path d="M4 2l12 15L4 32" fill="none" stroke="#fff" stroke-width="2"/></svg></div>
  <div class="abs case-btn">CORVANTIS &nbsp;– Export Credit Agency backed long term financing</div>
</section>

<div class="abs to-top"><svg width="34" height="24" viewBox="0 0 34 24"><path d="M17 2L32 22Q17 13 2 22z" fill="#1b8ad0"/></svg></div>
<p class="abs copyright">© <span>Corvantis</span> - &nbsp;2016. All Rights Reserved</p>
<div class="abs social dark" style="left:467px"></div>
<div class="abs social" style="left:538px"></div>
<div class="abs social" style="left:612px"></div>
<div class="abs social" style="left:685px"></div>

<div class="abs notch" style="left:586px;top:2634px;border-top:0;border-bottom:14px solid var(--blue)"></div>
<div class="abs footer-bar"></div>

</body>
</html>
```